LED-Leuchtboxen
Zielgruppe
Wir sind ein Ingenieurbüro und bieten Beratungsdienstleistungen an. Thema ist z.B. Sicherheit in öffentlichen Verwaltungen, Sicherheit von Mitarbeitern am Arbeitsplatz.
Orbitan Sicherheitsberatung GmbH
Ahornweg 17
70329 Stuttgart
Telefon 0711 5893 214
E-Mail info @lm-orbitan.com
Web www.lm-orbitan.com
Wir sind auf einer Messe und brauchen dafür zwei auffällige Designs für zwei LED-Leuchtboxen (Lumvor Dash). Die Besucher der Messe sind Mitarbeiter von öffentlichen Verwaltungen.
Aufgabenstellung
Für die beiden LED-Leuchtboxen brauchen wir farbige und auffällige Bilder/Designs, die aber nicht überfüllt sind und die man sich gerne anschaut. z.B. ein gutes Foto was entfernt etwas mit Sicherheit zu tun hat.
1. Box: Auffälliges Bild als Image-Werbung mit Icon, Firmennamen und vielleicht einem knackigen Spruch ('Heute war ich schon Bitch, Arschloch und wurde bedroht!') Beispiele: Siehe bLenza-Bilder im Anhang.
2. Box: Was wir tun.... (Sicherheit in öffentlichen Verwaltungen: - Notfall- und Krisenmanagement, - KRITIS-Bewertungen, - Fachplanung Sicherungstechnik, - Amok-Konzepte). Hier muss kein Foto im Hintergrund.
An die Vorgaben von Lumvor für die Druckdaten und die Maße ist sich unbedingt zu halten!!! Siehe beide Dateien im Anhang

```html
<!DOCTYPE html>
<html lang="de">
<head>
<meta charset="utf-8">
<title>Orbitan Messebanner</title>
<link href="https://fonts.googleapis.com/css2?family=Barlow+Condensed:ital,wght@0,400;0,600;0,700;1,500;1,600;1,700&family=Roboto:wght@400;500;700&display=swap" rel="stylesheet">
<style>
:root{
  --bg:#e6e6e4;
  --blue:#1553b8;
  --blue-dark:#0b3ea8;
  --blue-light:#2f7fd0;
  --orange:#f28a2e;
  --yellow:#fbc22b;
  --grey-text:#2d2f33;
  --concrete-1:#d9d9d7;
  --concrete-2:#b9bab8;
  --white:#ffffff;
}
*{box-sizing:border-box;margin:0;padding:0}
html,body{width:1200px;height:1117px;overflow:hidden;background:var(--bg)}
.stage{position:relative;width:1200px;height:1117px}
.banner{position:absolute;top:110px;width:370px;height:900px;overflow:hidden;box-shadow:0 6px 24px rgba(0,0,0,.18)}
.banner--image{left:190px}
.banner--services{left:640px;background:linear-gradient(180deg,var(--concrete-1),var(--concrete-2) 60%)}
.photo{position:absolute;left:0;top:0;width:100%;height:600px;background:linear-gradient(160deg,#cfcfcd 0%,#b8b8b6 45%,#9c9a97 100%)}
.brand{position:absolute;display:flex;align-items:center;gap:12px}
.brand__mark{width:56px;height:58px;border:4px solid var(--blue);flex:none}
.brand__name{font-family:'Roboto',sans-serif;font-weight:700;font-size:11px;line-height:1.3;letter-spacing:.8px;text-transform:uppercase;color:var(--grey-text)}
.banner--image .brand{left:62px;top:62px}
.stripe{position:absolute;left:0;width:100%;height:18px}
.stripe::before{content:"";position:absolute;left:0;top:0;width:100%;height:9px;background:linear-gradient(90deg,var(--orange),var(--yellow))}
.stripe::after{content:"";position:absolute;left:0;top:9px;width:100%;height:9px;background:var(--white)}
.blue-field{position:absolute;left:0;width:100%;bottom:0;background:linear-gradient(160deg,var(--blue) 0%,var(--blue-dark) 100%)}
.banner--image .stripe{top:563px}
.banner--image .blue-field{top:581px}
.slogan{position:absolute;left:52px;top:471px;width:270px;height:276px;background:linear-gradient(160deg,var(--blue),var(--blue-light));transform:skewX(-6deg);box-shadow:0 4px 14px rgba(0,0,0,.2)}
.slogan__text{position:absolute;left:52px;top:484px;width:262px;font-family:'Barlow Condensed',sans-serif;color:var(--white);text-align:center;line-height:.9}
.slogan__lead{display:block;font-style:italic;font-weight:500;font-size:19px;letter-spacing:.3px;margin-bottom:6px}
.slogan__big{display:block;font-style:italic;font-weight:700;font-size:90px;letter-spacing:-1px}
.slogan__accent{display:block;font-style:italic;font-weight:600;font-size:28px;color:var(--yellow);margin:2px 0 4px -40px}
.slogan__mid{font-weight:400;font-size:30px}
.slogan__big2{font-style:italic;font-weight:700;font-size:60px}
.slogan__last{display:block;font-style:italic;font-weight:700;font-size:60px}
.web-box{position:absolute;left:66px;top:780px;width:240px;height:50px;border:2px solid var(--orange);transform:skewX(-5deg);display:flex;align-items:center;justify-content:center}
.web-box span{transform:skewX(5deg);font-family:'Roboto',sans-serif;font-weight:500;font-size:19px;color:var(--white)}
.heading{position:absolute;left:0;top:66px;width:100%;text-align:center;font-family:'Barlow Condensed',sans-serif;font-weight:700;font-size:34px;color:var(--blue);letter-spacing:.5px}
.band{position:absolute;left:0;top:108px;width:100%;height:128px;background:linear-gradient(135deg,var(--blue-dark),var(--blue-light) 60%,var(--blue));display:flex;align-items:center;justify-content:center;text-align:center;font-family:'Barlow Condensed',sans-serif;font-style:italic;font-weight:700;font-size:38px;line-height:.95;color:var(--white);text-transform:uppercase}
.services{position:absolute;left:68px;top:262px;list-style:none}
.services li{display:flex;gap:18px;align-items:flex-start;margin-bottom:22px;font-family:'Barlow Condensed',sans-serif;font-style:italic;font-weight:600;font-size:26px;line-height:.95;color:var(--grey-text);text-transform:uppercase}
.services .bullet{width:26px;height:26px;border:2px solid var(--blue);flex:none;margin-top:1px}
.banner--services .stripe{top:572px}
.banner--services .blue-field{top:590px}
.banner--services .brand{left:66px;top:628px}
.banner--services .brand__mark{border-color:var(--white)}
.banner--services .brand__name{color:var(--white)}
.contact{position:absolute;left:66px;top:698px;width:243px;height:145px;border:2px solid var(--yellow);border-right-color:var(--orange);border-bottom-color:var(--orange);padding:14px 0 0 34px;font-family:'Roboto',sans-serif;font-weight:500;font-size:17px;line-height:22px;color:var(--white)}
.contact__row{display:flex;gap:12px;align-items:flex-start}
.contact__row svg{flex:none;margin-top:4px}
</style>
</head>
<body>
<main class="stage">

  <section class="banner banner--image">
    <div class="photo" role="img" aria-label="Foto: nachdenkliche Mitarbeiterin im weißen Hemd, im Hintergrund zwei Kollegen vor grauer Betonwand"></div>
    <div class="brand">
      <span class="brand__mark"></span>
      <p class="brand__name">Orbitan<br>Sicherheitsberatung<br>GmbH</p>
    </div>
    <div class="stripe"></div>
    <div class="blue-field"></div>
    <div class="slogan"></div>
    <p class="slogan__text">
      <span class="slogan__lead">HEUTE WAR ICH SCHON</span>
      <span class="slogan__big">BITCH,</span>
      <span class="slogan__accent">ARSCHLOCH</span>
      <span class="slogan__mid">UND</span> <span class="slogan__big2">WURDE</span>
      <span class="slogan__last">BEDROHT!</span>
    </p>
    <div class="web-box"><span>www.lm-orbitan.com</span></div>
  </section>

  <section class="banner banner--services">
    <h2 class="heading">WAS WIR TUN....</h2>
    <div class="band">Sicherheit<br>in öffentlichen<br>Verwaltungen:</div>
    <ul class="services">
      <li><span class="bullet"></span>Notfall- und<br>Krisenmanagement,</li>
      <li><span class="bullet"></span>KRITIS-Bewertungen,</li>
      <li><span class="bullet"></span>Fachplanung<br>Sicherungstechnik,</li>
      <li><span class="bullet"></span>Amok-Konzepte</li>
    </ul>
    <div class="stripe"></div>
    <div class="blue-field"></div>
    <div class="brand">
      <span class="brand__mark"></span>
      <p class="brand__name">Orbitan<br>Sicherheitsberatung<br>GmbH</p>
    </div>
    <address class="contact" style="font-style:normal">
      <div class="contact__row">
        <svg width="14" height="16" viewBox="0 0 14 16"><path d="M7 1a5 5 0 0 0-5 5c0 4 5 9 5 9s5-5 5-9a5 5 0 0 0-5-5z" fill="#fff"/><circle cx="7" cy="6" r="2" fill="#1553b8"/></svg>
        <span>Ahornweg 17<br>70329 Stuttgart</span>
      </div>
      <div class="contact__row">
        <svg width="14" height="14" viewBox="0 0 14 14"><circle cx="7" cy="7" r="6" fill="none" stroke="#fff" stroke-width="1.2"/><path d="M4.5 4c.3 2.5 2.5 5 5 5.5l.8-1.2-1.3-.8-.6.6c-1-.5-1.8-1.3-2.3-2.3l.6-.6-.8-1.3z" fill="#fff"/></svg>
        <span>0711 5893 214</span>
      </div>
      <div class="contact__row">
        <svg width="14" height="12" viewBox="0 0 14 12"><rect x="1" y="1.5" width="12" height="9" fill="none" stroke="#fff" stroke-width="1.2"/><path d="M1 2l6 5 6-5" fill="none" stroke="#fff" stroke-width="1.2"/></svg>
        <span>info @lm-orbitan.com</span>
      </div>
      <div class="contact__row">
        <svg width="14" height="14" viewBox="0 0 14 14" fill="none" stroke="#fff" stroke-width="1.1"><circle cx="7" cy="7" r="6"/><ellipse cx="7" cy="7" rx="2.6" ry="6"/><path d="M1 7h12M2 4h10M2 10h10"/></svg>
        <span>www.lm-orbitan.com</span>
      </div>
    </address>
  </section>

</main>
</body>
</html>
```